website for Facial Plastic Surgeon

We are in need of a modern, captivating and aesthetically pleasing website for KM Facial Plastics.
The website must be informative whilst flowing with ease and also entice patients to explore their options with the procedures we have available.
It is essential that the website is compatible across all devices and user friendly, especially when it comes to updating details within the website etc.
The pages we would require are:
Home, About, Procedures, Gallery & Contact
Procedures included on our website should be as follows:
Anti wrinkle injections and fillers
Necklifts
Brow lift
Facial scar revision
Rhytidectomy or Face lift
Chin implants
Rhinoplasty
Otoplasty or Pinnaplasty
Blepharoplasty or Upper and Lower Eyelid Surgery
Given the multiple locations of which we currently consult and operate from, our contact page should include a clear map outlining each clinic location.
- 48 Dunmore Street Echuca VIC 3550
- 312 Holloway Street Bendigo Vic 3550
- Level 3, 185 Marlow Street, Epping Vic 3076
- Level 6, 410 Thornbury Street Melbourne Vic 3000
Our new logo and examples of our stationary are also attached for your reference.
The following links below are examples of other websites that we like:
Example #1 https://www.brightmereaestheticclinic.co.uk/
Example #2 https://www.velmoracosmeticrooms.com.au/
Example #3 https://www.harrowdalefacialcentre.com.au/
There is opportunity for further work within another branch of our business for the successful candidate
Target Market(s)
Adults of all ages
Coding
Coded - Design and coding required
Number of Pages Required
5+ page
Requirements
Must have
- Modern
- Captivating
- Aesthetically pleasing

```html
<!DOCTYPE html>
<html lang="en">
<head>
<meta charset="UTF-8">
<title>KM Facial Plastics</title>
<link rel="stylesheet" href="https://fonts.googleapis.com/css2?family=Cinzel:wght@400;600&family=Montserrat:wght@400;500;600&display=swap">
<style>
:root{
  --pink:#e89aa4;
  --pink-soft:#f4a6a8;
  --lilac:#b994c4;
  --lilac-line:#d7b6d9;
  --ink:#2b2b2b;
  --text:#3c3c3c;
  --hero-bg:#f2f1f6;
  --band-grey:#efeff1;
  --band-lilac:#f0dff0;
  --white:#ffffff;
  --cap-dark:#5a5a5a;
  --cap-mid:#878787;
  --cap-light:#b2b2b2;
}
*{box-sizing:border-box;margin:0;padding:0}
html,body{width:1200px;height:2378px;overflow:hidden;background:var(--white)}
body{position:relative;font-family:'Montserrat',sans-serif;color:var(--text)}
.abs{position:absolute}
.serif{font-family:'Cinzel',serif;font-weight:400;color:var(--ink)}
.eyebrow{font-size:16px;letter-spacing:.5px;color:var(--lilac);text-transform:uppercase}

/* top */
.top-line{left:0;top:0;width:1200px;height:3px;background:var(--lilac-line)}
.nav a{position:absolute;top:48px;font-size:16px;font-weight:500;color:var(--ink);text-decoration:none}
.nav .active::after{content:"";position:absolute;left:-6px;right:-6px;top:31px;height:4px;background:var(--pink-soft)}
.cta{left:927px;top:41px;width:132px;height:32px;background:linear-gradient(90deg,var(--pink-soft) 55%,var(--lilac) 55%);color:#fff;font-size:14px;display:flex;align-items:center;justify-content:center}
.brand{width:140px;height:140px;border-radius:50%;background:#fff;display:flex;align-items:center;justify-content:center;text-align:center;font-family:'Montserrat',sans-serif;font-size:12px;font-weight:500;color:var(--ink);letter-spacing:.5px;line-height:1.3}
.brand-top{left:512px;top:8px;z-index:3}

/* hero */
.hero{left:0;top:90px;width:1200px;height:411px;background:var(--hero-bg)}
.hero-photo{left:711px;top:90px;width:360px;height:411px;background:radial-gradient(ellipse at 50% 45%,#f6e2d8 0%,#efd3c6 45%,#f2f1f6 75%)}
.flower{border-radius:50%;background:radial-gradient(circle,#f2d6e4 0%,#ead2ea 60%,rgba(242,241,246,0) 75%)}
.hero-eyebrow{left:164px;top:209px;font-size:20px;color:var(--pink);letter-spacing:.5px}
.hero-title{left:161px;top:238px;font-size:46px;line-height:54px;font-weight:400;font-family:'Cinzel',serif;color:var(--ink);white-space:nowrap}
.more{left:164px;top:366px;font-size:16px;font-weight:500;color:var(--ink);text-decoration:underline}
.dots{left:575px;top:443px;display:flex;gap:7px}
.dots span{width:11px;height:11px;border-radius:50%;background:#d5d3dc}
.dots span:first-child{background:var(--lilac)}

/* welcome */
.ba-photo{left:78px;top:563px;width:482px;height:335px;background:linear-gradient(90deg,#c39279 0%,#d4a58a 50%,#dfb598 100%)}
.ba-split{left:318px;top:563px;width:2px;height:335px;background:#fff}
.tag{color:#fff;background:var(--pink);font-family:'Cinzel',serif;font-size:28px;display:flex;align-items:center;justify-content:center}
.tag-after{left:414px;top:563px;width:146px;height:34px}
.tag-before{left:78px;top:864px;width:147px;height:34px}
.welcome-eyebrow{right:74px;top:581px;text-align:right}
.welcome-title{right:74px;top:608px;text-align:right;font-size:29px;line-height:37px}
.welcome-copy{left:595px;top:687px;width:531px;text-align:justify;text-align-last:right;font-size:13.2px;line-height:26.4px}

/* services */
.services{left:0;top:971px;width:1200px;height:462px;background:var(--band-grey)}
.services-photo{left:760px;top:971px;width:440px;height:462px;background:linear-gradient(110deg,rgba(239,239,241,0) 0%,#efd8cc 25%,#e8c7b6 60%,#f1dbcf 100%)}
.services-title{left:72px;top:1016px;font-size:29px;white-space:nowrap}
.grid{left:73px;top:1086px;display:grid;grid-template-columns:repeat(5,151px);gap:10px 10px}
.card{height:132px;background:#fff;border:1px solid #e6e6e8;display:flex;flex-direction:column;align-items:center;justify-content:flex-end;padding-bottom:10px;text-align:center;font-size:13px;line-height:16px;color:var(--ink)}
.card svg{margin-bottom:auto;margin-top:14px}

/* gallery */
.gal-eyebrow{left:0;width:1200px;top:1476px;text-align:center}
.gal-title{left:0;width:1200px;top:1504px;text-align:center;font-size:29px}
.shot{top:1562px;height:160px}
.cap{top:1724px;width:334px;height:33px;color:#fff;font-size:15px;font-weight:500;display:flex;align-items:center;justify-content:center;letter-spacing:.3px}
.see{left:534px;top:1785px;width:132px;height:31px;background:var(--pink-soft);color:#fff;font-size:15px;font-weight:500;display:flex;align-items:center;justify-content:center}

/* testimonial */
.clients{left:0;top:1863px;width:1200px;height:345px;background:var(--band-lilac)}
.clients-photo{left:803px;top:1863px;width:346px;height:345px;background:radial-gradient(ellipse at 55% 50%,#f1d5c9 0%,#e9c2b3 50%,#f0dff0 80%)}
.clients-title{left:72px;top:1898px;font-size:26px;white-space:nowrap}
.rule{left:72px;top:1950px;width:648px;height:2px;background:var(--lilac-line)}
.rule-dot{left:716px;top:1947px;width:8px;height:8px;border-radius:50%;background:var(--lilac-line)}
.quote{left:72px;top:1976px;width:650px;font-size:16px;line-height:26.5px}
.who{left:74px;top:2092px;font-size:14.5px;font-weight:600;color:var(--ink)}
.arrow-btn{top:2145px;width:36px;height:32px;border:1px solid var(--lilac-line);background:#fff;display:flex;align-items:center;justify-content:center}

/* footer */
.foot-links a{position:absolute;top:2262px;font-size:14.5px;color:var(--ink);text-decoration:none}
.copy{left:236px;top:2292px;font-size:13px;color:var(--text)}
.follow{left:1026px;top:2234px;font-size:15px;font-weight:500;color:var(--ink)}
.social{top:2262px;width:30px;height:30px;border-radius:50%;background:var(--pink-soft)}
.base-line{left:0;top:2374px;width:1200px;height:4px;background:var(--lilac-line)}
</style>
</head>
<body>
<div class="abs top-line"></div>

<!-- hero -->
<div class="abs hero"></div>
<div class="abs flower" style="left:-40px;top:90px;width:160px;height:150px"></div>
<div class="abs flower" style="left:-40px;top:280px;width:100px;height:110px"></div>
<div class="abs flower" style="left:1080px;top:90px;width:160px;height:150px"></div>
<div class="abs flower" style="left:1140px;top:280px;width:100px;height:110px"></div>
<div class="abs hero-photo" role="img" aria-label="Portrait of a woman in a white cap with facial contour arrows"></div>

<nav class="nav">
  <a class="active" style="left:163px">Home</a>
  <a style="left:253px">About</a>
  <a style="left:348px">Procedures</a>
  <a style="left:699px">Gallery</a>
  <a style="left:808px">Contact</a>
</nav>
<div class="abs cta">GET IN TOUCH</div>
<div class="abs brand brand-top">KM Facial<br>Plastics</div>

<div class="abs hero-eyebrow">ADVANCED TREATMENTS</div>
<h1 class="abs hero-title">Get the Best Skin<br>Treatments</h1>
<div class="abs more">More Info &gt;</div>
<div class="abs dots"><span></span><span></span><span></span></div>

<!-- welcome -->
<section class="welcome">
  <div class="abs ba-photo" role="img" aria-label="Before and after close-up of a woman's eyes and smile"></div>
  <div class="abs ba-split"></div>
  <div class="abs tag tag-after">After</div>
  <div class="abs tag tag-before">Before</div>
  <div class="abs eyebrow welcome-eyebrow">Welcome to KM Facial Plastics</div>
  <h2 class="abs serif welcome-title">World Class Treatments in<br>Affordable Price</h2>
  <p class="abs welcome-copy">Lorem ipsum dolor sit amet, consectetur adipiscing elit. Maecenas id est sed lacus volutpat lobortis. Occaecati cupiditate non provident, similique sunt in culpa qui officia deserunt mollitia animi, id est laborum et dolorum fuga. Lorem ipsum dolor sit amet, consectetur adipiscing elit. Maecenas id est sed lacus volutpat lobortis.Et harum quidem rerum facilis est et expedita distinctio. Lorem ipsum dolor sit amet, consectetur adipiscing elit. Maecenas id est sed lacus volutpat lobortis. Lorem ipsum dolor sit amet.</p>
</section>

<!-- services -->
<section>
  <div class="abs services"></div>
  <div class="abs services-photo" role="img" aria-label="Gloved hand marking a patient's face with a surgical pen"></div>
  <h2 class="abs serif services-title">Our Special Services</h2>
  <div class="abs grid">
    <div class="card"><svg width="60" height="60" viewBox="0 0 60 60" fill="none" stroke="#e8907c" stroke-width="2"><circle cx="38" cy="26" r="14"/><path d="M24 56c2-10 8-14 14-14s12 4 14 14"/><path d="M4 50l18-12"/></svg>Anti-Wrinkle<br>Injections &amp; Fillers</div>
    <div class="card"><svg width="60" height="60" viewBox="0 0 60 60" fill="none" stroke="#9b7bb0" stroke-width="2"><path d="M18 40c-6-16 0-34 16-34s20 16 14 30"/><path d="M24 56V40M44 56c0-8-4-12-8-14"/></svg>Necklifts</div>
    <div class="card"><svg width="70" height="50" viewBox="0 0 70 50" fill="none" stroke="#3faa8c" stroke-width="2"><path d="M4 26c16-18 46-18 62 0-16 18-46 18-62 0z"/><circle cx="35" cy="26" r="10"/><circle cx="35" cy="26" r="4"/><path d="M8 10c16-8 38-8 54 0"/></svg>Brow lift</div>
    <div class="card"><svg width="60" height="60" viewBox="0 0 60 60" fill="none" stroke="#2a8fa8" stroke-width="2"><ellipse cx="30" cy="28" rx="20" ry="24"/><circle cx="22" cy="32" r="3"/><circle cx="38" cy="32" r="3"/><path d="M22 44h16"/></svg>Facial Scar<br>Revision</div>
    <div class="card"><svg width="60" height="60" viewBox="0 0 60 60" fill="none" stroke="#b8a24a" stroke-width="2"><ellipse cx="30" cy="22" rx="12" ry="16"/><path d="M8 58c2-12 10-16 22-16s20 4 22 16"/></svg>Rhytidectomy<br>or Face lift</div>
    <div class="card"><svg width="60" height="60" viewBox="0 0 60 60" fill="none" stroke="#5b67b0" stroke-width="2"><circle cx="30" cy="30" r="24"/><rect x="16" y="26" width="28" height="10" rx="5"/><path d="M24 46h12"/></svg>Chin Implants</div>
    <div class="card"><svg width="60" height="60" viewBox="0 0 60 60" fill="none" stroke="#c99a3a" stroke-width="2"><path d="M14 24c0-14 8-20 16-20s16 6 16 20v10c0 12-8 20-16 20s-16-8-16-20z"/><path d="M30 26v14l-4 4h8"/></svg>Rhinoplasty</div>
    <div class="card"><svg width="50" height="66" viewBox="0 0 50 66" fill="none" stroke="#3a82c0" stroke-width="2"><path d="M12 24C12 10 22 4 30 4s14 8 14 18c0 10-10 12-12 22-2 10-8 16-14 16"/><path d="M24 22c0-6 10-6 10 2"/></svg>Otoplasty or<br>Pinnaplasty</div>
    <div class="card"><svg width="70" height="50" viewBox="0 0 70 50" fill="none" stroke="#8a8a8a" stroke-width="2"><path d="M4 26c16-18 46-18 62 0-16 18-46 18-62 0z"/><circle cx="35" cy="26" r="10"/><circle cx="35" cy="26" r="4"/></svg>Blepharoplasty</div>
    <div class="card"><svg width="70" height="50" viewBox="0 0 70 50" fill="none" stroke="#e07d98" stroke-width="2"><path d="M6 28c16-16 42-16 58 0-16 14-42 14-58 0z"/><path d="M8 14c16-8 38-8 54 0"/><path d="M14 34l-4 6M26 38l-2 6M44 38l2 6M56 34l4 6"/></svg>Upper and Lower<br>Eyelid Surgery</div>
  </div>
</section>

<!-- gallery -->
<section>
  <div class="abs eyebrow gal-eyebrow">Simple Procedure in Better Way</div>
  <h2 class="abs serif gal-title">Before and After Gallery</h2>
  <div class="abs shot" style="left:88px;width:164px;background:#c9a286" role="img" aria-label="Eye area before anti-wrinkle treatment"></div>
  <div class="abs shot" style="left:257px;width:165px;background:#d2ad92" role="img" aria-label="Eye area after anti-wrinkle treatment"></div>
  <div class="abs shot" style="left:433px;width:164px;background:linear-gradient(90deg,#b88470,#e8cabd 70%,#f4f0ee)" role="img" aria-label="Nose profile before rhinoplasty"></div>
  <div class="abs shot" style="left:602px;width:164px;background:linear-gradient(90deg,#b88470,#e8cabd 70%,#f4f0ee)" role="img" aria-label="Nose profile after rhinoplasty"></div>
  <div class="abs shot" style="left:778px;width:164px;background:linear-gradient(90deg,#e2c4b6,#ecd6cb)" role="img" aria-label="Neck before necklift surgery"></div>
  <div class="abs shot" style="left:947px;width:164px;background:linear-gradient(90deg,#efdcd2,#f3e4dc)" role="img" aria-label="Neck after necklift surgery"></div>
  <div class="abs cap" style="left:88px;background:var(--cap-dark)">ANTI-WRINKLE INJECTIONS &amp; FILLERS</div>
  <div class="abs cap" style="left:433px;background:var(--cap-mid)">RHINOPLASTY</div>
  <div class="abs cap" style="left:778px;background:var(--cap-light)">NECKLIFT SURGERY</div>
  <div class="abs see">See More &gt;</div>
</section>

<!-- testimonials -->
<section>
  <div class="abs clients"></div>
  <div class="abs clients-photo" role="img" aria-label="Woman's profile framed by a hexagon pattern"></div>
  <h2 class="abs serif clients-title">What our Clients are Saying</h2>
  <div class="abs rule"></div><div class="abs rule-dot"></div>
  <p class="abs quote">You were kind and attentive and most of all you are a superb doctor. Thank you again for the wonderful experience. You are by far the most exceptional! I strongly recommend to my friends.</p>
  <div class="abs who">- Elise Corwen</div>
  <div class="abs arrow-btn" style="left:72px"><svg width="12" height="18" viewBox="0 0 12 18" fill="none" stroke="#999" stroke-width="2"><path d="M10 2L3 9l7 7"/></svg></div>
  <div class="abs arrow-btn" style="left:111px;border-color:#c86a6a"><svg width="12" height="18" viewBox="0 0 12 18" fill="none" stroke="#333" stroke-width="2"><path d="M2 2l7 7-7 7"/></svg></div>
</section>

<!-- footer -->
<footer>
  <div class="abs flower" style="left:-30px;top:2290px;width:110px;height:100px"></div>
  <div class="abs flower" style="left:1110px;top:2290px;width:110px;height:100px"></div>
  <div class="abs brand" style="left:70px;top:2222px;width:120px;height:120px;font-size:11px">KM Facial<br>Plastics</div>
  <nav class="foot-links">
    <a style="left:236px">Home</a>
    <a style="left:314px">About</a>
    <a style="left:395px">Procedures</a>
    <a style="left:513px">Gallery</a>
    <a style="left:598px">Contact</a>
  </nav>
  <div class="abs copy">kmfacialplastics@2020. All Rights Reserved.</div>
  <div class="abs follow">Follow Us</div>
  <div class="abs social" style="left:1023px"></div>
  <div class="abs social" style="left:1059px"></div>
  <div class="abs social" style="left:1095px"></div>
  <div class="abs base-line"></div>
</footer>
</body>
</html>
```